Speisekarten-Design für mediterranes Restaurant
Zielgruppe
Wir eröffnen am 23.09.2022 ein Restaurant im Hotel SolBrunn Bad Farnhain in 94999 Fürstenzell unter dem Namen 'VELO'. Die Übersetzung aus dem Portugiesischem bedeutet 'Seele' - Velo soll also die Seele des Hauses werden und unsere Gäste aus nah&fern und ob jung oder alt mit mediterranen, besonderen Köstlichkeiten unseres Küchenchefs Matteo Carvalhal verwöhnen.
Auf der Speisekarte stehen Bruch & Frühstück (z.B. Joghurt mit Früchten und Agavensirup, Pancakes und Waffeln, Egg Benedikt aber auch bayerische Spezialitäten wie Weißwurst mit Breze). Weiterhin werden wir Tapas (vegatarisch, Fleisch, Fisch) anbieten. Als USP steht die original portugiesische Cataplana oder Hähnchen nach Art des Hauses auf der Karte. Hinzu kommen noch Desserts. Ebenso benötigen wir eine Wochenkarte sowie eine Getränkekarte (Softdrinks, Kaffee, Tee, Bier, Wein, Long Drinks, etc.) Ich denke eine Seite sollte für Frühstück/Brunch und eine für Vorspeisen, Tapas, Hauptspeisen vorgesehen werden und ein Blatt für die Wochenkarte. Weiterhin ein Blatt mit normalen Getränken und eine Weinkarte.
Wir suchen ein modernes, zeitloses Design für unsere neue Speisekarte. Diese soll auf einzelnen Blättern in einem Klemmbrett aus Holz eingespannt werden. Wichtig ist uns, dass wir die Gerichte und Getränke jederzeit in einem festen Design ändern und selbst drucken können.
Die hochgeladenen Speisekarten im Word-Format dienen nur der Orientierung für Anzahl, etc. Die Karten müssen selbstständig durch uns ergänzt oder geändert werden können. Anbei auch ein Beispielbild, welches über entwurfmarkt.de in Bildwand gefunden wurde.
Aufgabenstellung
als DIN-Format wählen wir A4.
Gerichte wir die Cataplana sollten eine Erklärung beinhalten, die auch noch gut aussieht und nicht nur in Klammern unter dem Gericht steht.

```html
<!DOCTYPE html>
<html lang="de">
<head>
<meta charset="utf-8">
<title>VELO – Speisekarten</title>
<link rel="stylesheet" href="https://fonts.googleapis.com/css2?family=Alfa+Slab+One&family=Ubuntu:wght@300;400;500;700&display=swap">
<style>
:root{
  --ink:#2b2a72;
  --bg-deep:#2a286f;
  --bg-glow:#3b43a8;
  --paper:#ffffff;
  --halo:rgba(96,140,255,.55);
}
*{box-sizing:border-box;margin:0;padding:0}
html,body{width:1200px;height:2422px;overflow:hidden}
body{
  position:relative;
  background:radial-gradient(ellipse at 50% 50%,var(--bg-glow) 0%,var(--bg-deep) 75%);
  font-family:'Ubuntu',sans-serif;color:var(--ink);
}
.page{position:absolute;width:453px;height:641px;background:var(--paper);box-shadow:0 0 55px var(--halo)}
.page-breakfast{left:114px;top:97px}
.page-eggs{left:645px;top:153px}
.page-starters{left:111px;top:844px}
.page-meatfish{left:628px;top:920px}
.page-mains{left:111px;top:1605px}
.page-drinks{left:628px;top:1678px}

.brand{position:absolute;left:0;right:0;text-align:center;font-weight:700;font-size:27px;letter-spacing:2px}
.menu-title{position:absolute;left:0;right:0;text-align:center;font-family:'Alfa Slab One',serif;font-size:19px;letter-spacing:2px;color:transparent;-webkit-text-stroke:.8px var(--ink)}
.hours{position:absolute;left:0;right:0;text-align:center;font-size:8.5px}
.section{position:absolute;text-align:center;font-weight:500;font-size:15.5px;letter-spacing:1.8px;line-height:1.2}
.section.full{left:0;right:0}

.dish{position:absolute;width:150px}
.col-l{left:58px}
.col-r{left:246px}
.dish-row{display:flex;justify-content:space-between;align-items:flex-start}
.dish-name{font-size:9px;font-weight:700;letter-spacing:1px;line-height:1.2;max-width:112px;text-transform:uppercase}
.price{font-size:9px;font-weight:500;letter-spacing:.5px}
.dish-desc{font-size:6.8px;font-weight:300;line-height:1.3;margin-top:2px;max-width:122px}
.extras{list-style:none;margin-top:5px}
.extras li{display:flex;justify-content:space-between;align-items:flex-end;font-size:8.3px;line-height:1.2;margin-bottom:4px}
.extras li span:first-child{max-width:100px}
.extras.tight li{margin-bottom:2.5px}
.price-pair{display:flex;gap:14px}
.size-head{position:absolute;font-size:8.5px;display:flex;gap:14px;letter-spacing:.5px}

.quote{position:absolute;left:246px;top:524px;width:148px;height:36px;border:1.2px solid var(--ink);font-size:8.3px;line-height:1.25;text-align:center;padding-top:7px}
.quote small{font-size:5.5px}
.plain-list{list-style:none}
.plain-list li{display:flex;justify-content:space-between;font-size:8.3px;margin-bottom:4.6px}
.stack-names{font-size:9px;font-weight:700;letter-spacing:1px;line-height:1.55}
.stack-prices{font-size:9px;font-weight:500;line-height:1.55;text-align:right}
.stack{position:absolute;display:flex;justify-content:space-between;width:150px}
.wine-sub{font-size:6.8px;font-weight:500;margin-top:2px}
</style>
</head>
<body>

<!-- Frühstück & Brunch -->
<section class="page page-breakfast">
  <div class="brand" style="top:80px">VELO</div>
  <div class="menu-title" style="top:163px">FRÜHSTÜCKS- &amp; BRUNCH</div>
  <div class="hours" style="top:190px">Von 8:00 bis 13:00 Uhr</div>
  <h2 class="section full" style="top:225px">GUTEN MORGEN!</h2>

  <div class="dish col-l" style="top:265px">
    <div class="dish-row"><h3 class="dish-name">Süßer Beginn</h3><span class="price">5.5</span></div>
    <p class="dish-desc">mit knackigem Obstsalat, frischem Croissant (Marmelade, Honig &amp; Nougatina), einem kleinen Becher Jogurt oder einem Bircher Müsli</p>
  </div>
  <div class="dish col-r" style="top:265px">
    <div class="dish-row"><h3 class="dish-name">Bircher Müsli</h3><span class="price">5.5</span></div>
    <p class="dish-desc">auf Hafermilch-Basis, dazu frische Früchte, Zimt &amp; schwarzer Sesam</p>
  </div>
  <div class="dish col-l" style="top:363px">
    <div class="dish-row"><h3 class="dish-name">Joghurt mit frischen Früchten &amp; Agavensirup</h3><span class="price" style="margin-top:20px">5.5</span></div>
    <ul class="extras"><li><span>mit Granola</span><span>+1.0</span></li><li><span>mit Sojajoghurt</span><span>+1.0</span></li></ul>
  </div>
  <div class="dish col-l" style="top:481px">
    <div class="dish-row"><h3 class="dish-name">Pancakes &amp; Waffeln</h3><span class="price">5.5</span></div>
    <ul class="extras"><li><span>Schoko</span><span>+1.0</span></li><li><span>Blaubeer</span><span>+1.0</span></li></ul>
  </div>
  <div class="dish col-r" style="top:348px">
    <h3 class="dish-name">Frische Backwaren</h3>
    <ul class="plain-list" style="margin-top:8px">
      <li><span>Gemischtes Brot</span><span>2.5</span></li>
      <li><span>Breze</span><span>1.5</span></li>
      <li><span>Croissant</span><span>2.0</span></li>
      <li><span>Franzbrötchen</span><span>2.0</span></li>
      <li><span>Pain au Chocolat</span><span>2.0</span></li>
      <li><span>Quiche</span><span>4.0</span></li>
      <li style="margin-bottom:1px"><span>Kuchen</span><span>3.5</span></li>
    </ul>
    <p class="dish-desc">Fragen Sie unsre Mitarbeiter nach dem heutigen Angebot</p>
  </div>
  <div class="quote">„Essen und Trinken hält Leib<br>und Seele zusammen.“ <small>(Theodoros)</small></div>
</section>

<!-- Eier & Herzhaftes -->
<section class="page page-eggs">
  <h2 class="section full" style="top:78px">BIO-EIER VOM GLÜCKLICHEN HUHN</h2>
  <div class="dish col-l" style="top:115px">
    <div class="dish-row"><h3 class="dish-name">Eier im Glas</h3><span class="price">5.5</span></div>
    <p class="dish-desc">zwei pochierte Eier im Glas auf Salatbett mit Kräutern &amp; Granatapfel, dazu Brot</p>
  </div>
  <div class="dish col-r" style="top:115px">
    <div class="dish-row"><h3 class="dish-name">Rührei / Spiegeleier</h3><span class="price">5.5</span></div>
    <ul class="extras"><li><span>mit gebratenem Speck</span><span>+1.0</span></li><li><span>mit karamellisierten Tomaten</span><span>+1.0</span></li><li><span>mit Räucherlachs</span><span>+1.0</span></li></ul>
  </div>
  <div class="dish col-l" style="top:187px">
    <div class="dish-row"><h3 class="dish-name">Egg Benedict</h3><span class="price">5.5</span></div>
    <p class="dish-desc">English Muffin Toastie mit Avocado Creme, Serrano Schinken und hausgemachter Sauce Hollandaise</p>
    <ul class="extras"><li><span>mit halber Avocado</span><span>+1.0</span></li><li><span>mit karamellisierten Tomaten</span><span>+1.0</span></li><li><span>mit Speck</span><span>+1.0</span></li></ul>
  </div>
  <div class="dish col-r" style="top:210px">
    <div class="dish-row"><h3 class="dish-name">Egg Royale</h3><span class="price">5.5</span></div>
    <p class="dish-desc">English Muffin Toastie mit Avocado Creme, Räucherlachs und hausgemachter Sauce Hollandaise</p>
    <ul class="extras"><li><span>mit halber Avocado</span><span>+1.0</span></li><li><span>mit karamellisierten Tomaten</span><span>+1.0</span></li></ul>
  </div>
  <h2 class="section full" style="top:326px">EINFACH WEIL ES GUT IST</h2>
  <div class="dish col-l" style="top:364px">
    <div class="dish-row"><h3 class="dish-name">Wurstbrett</h3><span class="price">5.5</span></div>
    <p class="dish-desc">Serrano-, Puten- &amp; Rinderschinken</p>
  </div>
  <div class="dish col-r" style="top:364px">
    <div class="dish-row"><h3 class="dish-name">Shakshuka</h3><span class="price">5.5</span></div>
    <p class="dish-desc">israelisches Frühstück aus selbstgemachtem orientalischen Tomatensugo, zwei gestockten Eiern, Zwiebeln, Paprika &amp; dazu Brot</p>
  </div>
  <div class="dish col-l" style="top:408px">
    <div class="dish-row"><h3 class="dish-name">Lachsteller</h3><span class="price">5.5</span></div>
    <p class="dish-desc">mit frischem Kren und Zitrone</p>
  </div>
  <div class="dish col-l" style="top:454px">
    <div class="dish-row"><h3 class="dish-name">Käsebrett</h3><span class="price">5.5</span></div>
    <p class="dish-desc">Edamer, Brie &amp; Obazda</p>
  </div>
  <div class="dish col-r" style="top:444px">
    <div class="dish-row"><h3 class="dish-name">Frühschoppen</h3><span class="price">5.5</span></div>
    <p class="dish-desc">2 Stück Weißwürstl mit Brezn, süßem Senf &amp; Butter</p>
  </div>
  <div class="dish col-l" style="top:499px">
    <div class="dish-row"><h3 class="dish-name">Avocado Stulle</h3><span class="price">5.5</span></div>
    <p class="dish-desc">Sauerteigbrot mit halber Avocado, Avocado Creme, gemischtem Salat</p>
    <ul class="extras"><li><span>mit Serrano-Schinken</span><span>+1.0</span></li><li><span>mit Räucherlachs</span><span>+1.0</span></li><li><span>mit Spiegelei / Rührei</span><span>+1.0</span></li></ul>
  </div>
  <div class="dish col-r" style="top:499px">
    <div class="dish-row"><h3 class="dish-name">Frühstück für 2</h3><span class="price">45.0</span></div>
    <p class="dish-desc">Brotkörberl + 2 Croissant + Butter, Wurstbrett + Käsebrett, Rühei, Pancake „all in one“, Obstsalat, Marmelade, Honig &amp; Nougatina, 2 x 0,1L frisch gepresster Orangensaft + 2 x Heißgetränk</p>
  </div>
</section>

<!-- Vorspeisen -->
<section class="page page-starters">
  <div class="menu-title" style="top:45px">VORSPEISEN</div>
  <div class="hours" style="top:70px">Von 16:00 bis 22:00 Uhr</div>
  <h2 class="section full" style="top:104px">TAPAS &amp; BROTZEIT</h2>

  <div class="dish col-l" style="top:147px"><div class="dish-row"><h3 class="dish-name">Tagessuppe</h3><span class="price">5.5</span></div></div>
  <div class="dish col-l" style="top:182px">
    <div class="dish-row"><h3 class="dish-name">Brotkorb mit Knoblauchbutter</h3><span class="price" style="margin-top:6px">5.5</span></div>
    <ul class="extras tight">
      <li><span>Pesto Basilico</span><span>2.5</span></li><li><span>Tomatenpesto</span><span>1.5</span></li>
      <li><span>Chimichurri</span><span>2.0</span></li><li><span>Aioli</span><span>2.0</span></li>
      <li><span>Pico de Gallo</span><span>2.0</span></li><li><span>Oliventapenade</span><span>4.0</span></li>
      <li><span>Hummus</span><span>3.5</span></li>
    </ul>
  </div>
  <div class="dish col-l" style="top:331px">
    <div class="dish-row"><h3 class="dish-name">Pimientos del Piquillo</h3><span class="price" style="margin-top:6px">5.5</span></div>
    <p class="dish-desc">Stockfisch-Kroketten, Samosa oder Fleisch &amp; Garnelen-Pastete</p>
  </div>
  <div class="dish col-l" style="top:397px">
    <div class="dish-row"><h3 class="dish-name">Pimientos de Padrón</h3><span class="price" style="margin-top:6px">5.5</span></div>
    <p class="dish-desc">Stockfisch-Kroketten, Samosa oder Fleisch &amp; Garnelen-Pastete</p>
  </div>
  <div class="dish col-l" style="top:462px">
    <div class="dish-row"><h3 class="dish-name">Bruschetta Pico-de-Gallo</h3><span class="price" style="margin-top:6px">5.5</span></div>
    <p class="dish-desc">geröstetes Knoblauchbrot mit marinierter Tomaten-Gurken Salsa</p>
  </div>
  <div class="dish col-l" style="top:528px">
    <div class="dish-row"><h3 class="dish-name">Obazda</h3><span class="price">5.5</span></div>
    <p class="dish-desc">mit Breze &amp; roten Zwiebeln</p>
  </div>
  <div class="dish col-l" style="top:573px">
    <div class="dish-row"><h3 class="dish-name">Büffelmozzarella</h3><span class="price">5.5</span></div>
    <p class="dish-desc">Mit Tomate, Rucola und BalsamicoCreme</p>
  </div>

  <div class="dish col-r" style="top:147px"><div class="dish-row"><h3 class="dish-name">Gewürzte Oliven</h3><span class="price">5.5</span></div></div>
  <div class="dish col-r" style="top:182px">
    <div class="dish-row"><h3 class="dish-name">Karotten</h3><span class="price">5.5</span></div>
    <p class="dish-desc">Mit aromatischen Kräutern in Weißwein Essig und Kümmel</p>
  </div>
  <div class="dish col-r" style="top:236px">
    <div class="dish-row"><h3 class="dish-name">Papas Arrugadas</h3><span class="price">5.5</span></div>
    <p class="dish-desc">kanarische Salzkartoffeln</p>
  </div>
  <div class="dish col-r" style="top:282px">
    <div class="dish-row"><h3 class="dish-name">Wurst &amp; Käsebrett</h3><span class="price">5.5</span></div>
    <p class="dish-desc">Schinken und Wurst aus der Region Edamer, Brie &amp; Obazda</p>
  </div>
  <div class="dish col-r" style="top:338px">
    <div class="dish-row"><h3 class="dish-name">Kroketten</h3><span class="price">5.5</span></div>
    <p class="dish-desc">Stockfisch-Kroketten, Samosa oder Fleisch &amp; Garnelen-Pastete</p>
  </div>
  <div class="dish col-r" style="top:392px">
    <div class="dish-row"><h3 class="dish-name">Antipasti-Spiesse</h3><span class="price">5.5</span></div>
    <p class="dish-desc">Zucchini, Kirschtomaten, rote Zwiebeln, Paprika, Mozzarella</p>
  </div>
  <div class="dish col-r" style="top:446px">
    <div class="dish-row"><h3 class="dish-name">Gegrillter Ziegenkäse</h3><span class="price" style="margin-top:6px">5.5</span></div>
    <p class="dish-desc">Paniert mit Marmelade und Walnüssen</p>
  </div>
  <div class="dish col-r" style="top:512px">
    <div class="dish-row"><h3 class="dish-name">Huevos Rancheros</h3><span class="price">5.5</span></div>
    <p class="dish-desc">Epische Kombination aus würzigem Tomaten Eintopf mit pochiertem Ei, garniert mit Pico de Gallo</p>
  </div>
</section>

<!-- Fleisch & Fisch -->
<section class="page page-meatfish">
  <h2 class="section full" style="top:104px">FLEISCH &amp; FISCH</h2>
  <div class="dish col-l" style="top:148px"><div class="dish-row"><h3 class="dish-name">Pflaumen im Speckmantel</h3><span class="price">5.5</span></div></div>
  <div class="dish col-l" style="top:219px">
    <div class="dish-row"><h3 class="dish-name">Chorizo</h3><span class="price">5.5</span></div>
    <p class="dish-desc">gegrillte pikante Paprikawurst aus Spanien</p>
  </div>
  <div class="dish col-l" style="top:304px">
    <div class="dish-row"><h3 class="dish-name">Albóndigas</h3><span class="price">5.5</span></div>
    <p class="dish-desc">Saftige Wild Fleischbällchen in Tomatensauce</p>
  </div>
  <div class="dish col-l" style="top:385px">
    <div class="dish-row"><h3 class="dish-name">Cassoulet</h3><span class="price">5.5</span></div>
    <p class="dish-desc">Bohneneintopf mit regionalem Fleisch und würziger Chorizo</p>
  </div>
  <div class="dish col-r" style="top:148px">
    <div class="dish-row"><h3 class="dish-name">Knusprige Garnelen</h3><span class="price">5.5</span></div>
    <p class="dish-desc">Tempura-Panko Panade Garnelen mit hausgemachter Aioli</p>
  </div>
  <div class="dish col-r" style="top:229px">
    <div class="dish-row"><h3 class="dish-name">Gambas Pil Pil.</h3><span class="price">5.5</span></div>
    <p class="dish-desc">Garnelen mit Knoblauch und Chili</p>
  </div>
  <div class="dish col-r" style="top:303px">
    <div class="dish-row"><h3 class="dish-name">Boquerones en Vinagre</h3><span class="price">5.5</span></div>
    <p class="dish-desc">In Olivenöl und Weinessig eingelegte Sardellenfilets, mit Knoblauch und Petersilie</p>
  </div>
</section>

<!-- Hauptspeise -->
<section class="page page-mains">
  <div class="menu-title" style="top:45px">HAUPTSPEISE</div>
  <div class="hours" style="top:70px">Von 19:00 bis 22:00 Uhr</div>
  <h2 class="section full" style="top:104px">AUS DER METZGEREI</h2>
  <div class="dish col-l" style="top:148px">
    <div class="dish-row"><h3 class="dish-name">Hähnchen nach Art des Hauses</h3><span class="price">5.5</span></div>
    <p class="dish-desc">Hähnchen in Olivenöl mit Knoblauch gegrillt, belegt mit Mini-Pickles, Oliven und Koriander</p>
  </div>
  <div class="dish col-l" style="top:231px">
    <div class="dish-row"><h3 class="dish-name">Beef Tagliata</h3><span class="price">5.5</span></div>
    <p class="dish-desc">Hähnchen in Olivenöl mit Knoblauch gegrillt, belegt mit Mini-Pickles, Oliven und Koriander</p>
  </div>
  <div class="dish col-r" style="top:148px">
    <div class="dish-row"><h3 class="dish-name">Rinderfilet 200g</h3><span class="price">5.5</span></div>
    <p class="dish-desc">Hähnchen in Olivenöl mit Knoblauch gegrillt, belegt mit Mini-Pickles, Oliven und Koriander</p>
  </div>
  <div class="dish col-r" style="top:220px;width:150px">
    <div class="dish-row"><h3 class="dish-name">Cassoulet</h3><span class="price">5.5</span></div>
    <p class="dish-desc" style="max-width:150px">Hähnchen in Olivenöl mit Knoblauch gegrillt, belegt mit Mini-Pickles, Oliven</p>
  </div>
  <h2 class="section full" style="top:300px">NUR AUF VORBESTELLUNG<br>AB 2 PERSONEN</h2>
  <div class="dish col-l" style="top:361px">
    <div class="dish-row"><h3 class="dish-name">Cataplana</h3><span class="price">5.5</span></div>
    <p class="dish-desc">mit Meeresfrüchten<br>mit Seeteufel/Seebarsch<br>mit Kabeljau</p>
  </div>
  <div class="dish col-l" style="top:424px">
    <div class="dish-row"><h3 class="dish-name">Cassoulet</h3><span class="price">5.5</span></div>
    <p class="dish-desc" style="max-width:150px">Hähnchen in Olivenöl mit Knoblauch gegrillt, belegt mit Mini-Pickles, Oliven</p>
  </div>
  <div class="dish col-r" style="top:361px">
    <div class="dish-row"><h3 class="dish-name">Rinderfilet 200g</h3><span class="price">5.5</span></div>
    <p class="dish-desc">Hähnchen in Olivenöl mit Knoblauch gegrillt, belegt mit Mini-Pickles, Oliven und Koriander</p>
  </div>
  <div class="dish col-r" style="top:432px">
    <div class="dish-row"><h3 class="dish-name">Cassoulet</h3><span class="price">5.5</span></div>
    <p class="dish-desc" style="max-width:150px">Hähnchen in Olivenöl mit Knoblauch gegrillt, belegt mit Mini-Pickles, Oliven</p>
  </div>
  <h2 class="section" style="top:490px;left:58px;width:150px">KINDER MENU</h2>
  <h2 class="section" style="top:490px;left:246px;width:150px">BEILAGEN</h2>
  <div class="dish col-l" style="top:526px"><div class="dish-row"><h3 class="dish-name">Spaghetti mit Fleischbällchen</h3><span class="price">5.5</span></div></div>
  <div class="dish col-r" style="top:526px">
    <ul class="plain-list">
      <li><span>Bunter Gartensalat</span><span>3.5</span></li>
      <li><span>Tomatensalat</span><span>2.5</span></li>
      <li><span>Tageskartoffelbeilage</span><span>2.5</span></li>
      <li><span>Rustikale Kartoffelchips</span><span>2.0</span></li>
      <li><span>Süßkartoffelpommes</span><span>2.5</span></li>
      <li><span>Reis</span><span>2.5</span></li>
    </ul>
  </div>
</section>

<!-- Getränke -->
<section class="page page-drinks">
  <div class="menu-title" style="top:45px">GETRÄNKE</div>
  <h2 class="section full" style="top:104px">LEICHT &amp; FRISCH</h2>
  <div class="size-head" style="top:133px;left:346px"><span>0,2l</span><span>0,4l</span></div>
  <div class="dish col-l" style="top:148px">
    <div class="dish-row"><h3 class="dish-name">Limos</h3><span class="price">3.9</span></div>
    <p class="dish-desc">Kolaro, Light &amp; Zero, Orangelo, Zitrello, Mixolo</p>
  </div>
  <div class="dish col-r" style="top:148px">
    <div class="dish-row"><h3 class="dish-name">Saft &amp; Nektar</h3><span class="price price-pair"><span>3.9</span><span>4.9</span></span></div>
    <p class="dish-desc">Orange, Apfel, Kirsche, Maracuja, Johannisbeere</p>
  </div>
  <div class="dish col-l" style="top:202px">
    <div class="dish-row"><h3 class="dish-name">XY Lemonade</h3><span class="price">3.9</span></div>
    <p class="dish-desc">Lorem ipsum dolor sit amet, con-setetur sadipscing elitr, sed diam nonumy eirmod tempor</p>
  </div>
  <div class="dish col-r" style="top:202px">
    <div class="dish-row"><h3 class="dish-name">XY Eistee</h3><span class="price">3.9</span></div>
    <p class="dish-desc">Lorem ipsum dolor sit amet, con-setetur sadipscing elitr, sed diam nonumy eirmod tempor</p>
  </div>
  <h2 class="section full" style="top:262px">KAFFEE &amp; TEE</h2>
  <div class="stack" style="top:303px;left:58px">
    <div class="stack-names">CAFE CREME<br>ESPRESSO<br>LATTE MACCHIATO<br>HEISSER KAKAO</div>
    <div class="stack-prices">3.9<br>3.9<br>3.9<br>3.9<br>3.9</div>
  </div>
  <div class="stack" style="top:303px;left:246px">
    <div>
      <div class="stack-names">CAPPUCCINO<br>CAFÉ AU LAIT<br>TEESPEZIALITÄTEN</div>
      <p class="dish-desc" style="margin-top:0">Schwarztee, Grüntee, Kräutertee &amp; Früchtetee</p>
    </div>
    <div class="stack-prices" style="padding-top:3px">3.9<br>3.9<br>3.9</div>
  </div>
  <h2 class="section full" style="top:383px">BIERE</h2>
  <div class="stack" style="top:425px;left:58px">
    <div class="stack-names">PILS VOM FASS<br>BIER ALKOHOLFREI</div>
    <div class="stack-prices">3.9<br>3.9</div>
  </div>
  <div class="stack" style="top:425px;left:246px">
    <div class="stack-names">WEIZEN<br>WEIZEN ALKOHOLFREI</div>
    <div class="stack-prices" style="padding-top:3px">3.9<br>3.9</div>
  </div>
  <h2 class="section" style="top:472px;left:58px;width:150px">WEISSWEIN</h2>
  <h2 class="section" style="top:472px;left:246px;width:150px">ROTWEIN</h2>
  <div class="size-head" style="top:501px;left:158px"><span>0,2l</span><span>0,7l</span></div>
  <div class="size-head" style="top:501px;left:346px"><span>0,2l</span><span>0,7l</span></div>
  <div class="dish col-l" style="top:516px">
    <div class="dish-row"><h3 class="dish-name">Riesling</h3><span class="price price-pair"><span>3.9</span><span>14.9</span></span></div>
    <p class="wine-sub">Lorem ipsum dolor</p>
    <p class="dish-desc" style="margin-top:1px">Lorem ipsum dolor sit amet, con-setetur sadipscing elitr, sed diam quyam erat, sed diam voluptua</p>
  </div>
  <div class="dish col-r" style="top:516px">
    <div class="dish-row"><h3 class="dish-name">Riesling</h3><span class="price price-pair"><span>3.9</span><span>14.9</span></span></div>
    <p class="wine-sub">Lorem ipsum dolor</p>
    <p class="dish-desc" style="margin-top:1px">Lorem ipsum dolor sit amet, con-setetur sadipscing elitr, sed diam quyam erat, sed diam voluptua</p>
  </div>
</section>

</body>
</html>
```